Create a cover for English Grammar Workbook

This book describes a system to learn English in a proper way - we call it The ''Keystone Loop'' System.

It focuses on not only teaching grammar and its structures, but also giving students tips on how to use it and the best ways to remember what they learn.

The cover should have 3 realistic pillars (3D), with one closer to the front to show that this book is the 1st (front) Pillar.

The title is: "Unlocking Tricky Syntax Rules: *A Calm Path toward Fluency"*

Author's name: Dorian Pell

```html
<!DOCTYPE html>
<html lang="en">
<head>
<meta charset="utf-8">
<title>Unlocking Tricky Syntax Rules — Dorian Pell</title>
<link rel="stylesheet" href="https://fonts.googleapis.com/css2?family=Roboto:wght@900&family=Gochi+Hand&display=swap">
<style>
  :root {
    --frame-red: #d40d10;
    --slate: #30313a;
    --white: #ffffff;
    --pillar-light: #f4f4f4;
    --pillar-shade: #c9cacd;
  }
  html, body {
    margin: 0;
    padding: 0;
    overflow: hidden;
    background: var(--frame-red);
  }
  .cover {
    position: relative;
    width: 752px;
    height: 1200px;
    background: var(--frame-red);
    overflow: hidden;
    font-family: "Roboto", Arial, sans-serif;
    font-weight: 900;
  }
  .cover-panel {
    position: absolute;
    left: 32px;
    top: 23px;
    width: 685px;
    height: 1155px;
    background: var(--slate);
  }
  .title {
    position: absolute;
    left: 114px;
    top: 128px;
    margin: 0;
    font-size: 80px;
    line-height: 79px;
    letter-spacing: -1px;
    text-transform: uppercase;
    color: var(--white);
  }
  .title-line { display: block; white-space: nowrap; }
  .title-line--accent { color: var(--frame-red); }
  .title-script {
    display: inline-block;
    margin-left: 12px;
    font-family: "Gochi Hand", cursive;
    font-weight: 400;
    font-size: 70px;
    letter-spacing: 1px;
    text-transform: none;
    transform: rotate(-10deg) translateY(-10px);
    transform-origin: left bottom;
  }
  .pillars {
    position: absolute;
    left: 0;
    top: 0;
    width: 752px;
    height: 860px;
  }
  .pillar {
    position: absolute;
    bottom: 6px;
    background: linear-gradient(90deg, var(--pillar-shade), var(--pillar-light) 40%, var(--white) 60%, var(--pillar-shade));
  }
  .pillar--left  { left: 184px; width: 88px;  height: 376px; }
  .pillar--front { left: 332px; width: 107px; height: 449px; }
  .pillar--right { left: 499px; width: 90px;  height: 376px; }
  .ground-line {
    position: absolute;
    left: 32px;
    top: 854px;
    width: 685px;
    height: 8px;
    background: var(--white);
  }
  .subtitle {
    position: absolute;
    left: 63px;
    width: 600px;
    top: 886px;
    margin: 0;
    text-align: center;
    font-size: 29px;
    letter-spacing: -0.3px;
    text-transform: uppercase;
    color: var(--white);
  }
  .author {
    position: absolute;
    left: 32px;
    width: 688px;
    top: 1083px;
    margin: 0;
    text-align: center;
    font-size: 62px;
    letter-spacing: -0.5px;
    text-transform: uppercase;
    color: var(--white);
  }
</style>
</head>
<body>
  <main class="cover">
    <div class="cover-panel"></div>

    <h1 class="title">
      <span class="title-line title-line--accent">Unlocking</span>
      <span class="title-line">Tricky</span>
      <span class="title-line">Syntax<span class="title-script">Rules</span></span>
    </h1>

    <div class="pillars" role="img" aria-label="Three realistic white classical pillars, the middle one taller and closer to the front">
      <div class="pillar pillar--left"></div>
      <div class="pillar pillar--front"></div>
      <div class="pillar pillar--right"></div>
    </div>

    <div class="ground-line"></div>

    <p class="subtitle">A Calm Path toward Fluency</p>

    <p class="author">Dorian Pell</p>
  </main>
</body>
</html>
```